Shipping cards

Expedited delivery of various business related products , packages ,parcels etc. Intrastate or Interstate.

Target Market(s)

business and or private customer base.with expedited needs and short term or long term needs.

Industry/Entity Type

Business

Contact Information for Business Card

would like the silhouette of my dog between the business name Amber{ } Fox . Amber Fox Freight ,Expedited Delivery, tel330-958-3637 fax TBD , dispatch@quillmail.test, Dennis J. Holt- Owner

Font styles to use
Serif

Requirements
Must have
• dog silhouette between Amber Fox or before and after name of company.
Should not have
• remove oval from silhouette around dog

```html
<!DOCTYPE html>
<html lang="en">
<head>
<meta charset="utf-8">
<title>Amber Fox Freight – Business Card</title>
<link rel="stylesheet" href="https://fonts.googleapis.com/css2?family=Tinos:wght@400;700&display=swap">
<style>
  :root {
    --page-bg: #d9d9dc;
    --card-navy: #1c1c58;
    --navy-deep: #15154a;
    --ghost-navy: #25256c;
    --band-light: #8db3ea;
    --band-dark: #2a2a7c;
    --ink-light: #9dbcf0;
    --ink-dark: #16164a;
  }
  * { margin: 0; padding: 0; box-sizing: border-box; }
  html, body {
    width: 1200px; height: 900px; overflow: hidden;
    background: var(--page-bg);
  }
  .card {
    position: absolute; left: 75px; top: 150px;
    width: 1050px; height: 600px;
    background: var(--card-navy);
    overflow: hidden;
    font-family: "Tinos", "Times New Roman", serif;
    box-shadow: 0 14px 30px rgba(0,0,0,0.35);
  }
  .ripple-decoration {
    position: absolute; left: 260px; top: 180px;
    width: 640px; height: 520px;
    background: radial-gradient(ellipse at center, rgba(40,40,110,0.55) 0%, rgba(28,28,88,0) 70%);
  }
  .ghost-name {
    position: absolute; left: 300px; top: 130px;
    font-size: 210px; font-weight: 400; line-height: 1;
    color: var(--ghost-navy); white-space: nowrap;
  }
  .brand {
    position: absolute; left: 110px; top: 28px;
    display: flex; align-items: center; gap: 26px;
  }
  .brand-name {
    font-size: 96px; font-weight: 400; line-height: 1;
    color: var(--ink-light); letter-spacing: 2px;
  }
  .brand-dot {
    width: 34px; height: 34px; border-radius: 50%;
    background: var(--ink-light);
  }
  .brand-rule {
    position: absolute; left: 96px; top: 142px;
    width: 600px; height: 3px; background: var(--ink-light);
  }
  .band {
    position: absolute; left: 0; top: 170px;
    width: 1050px; height: 52px;
    background: linear-gradient(90deg, var(--band-light) 0%, var(--band-light) 30%, var(--band-dark) 62%, var(--band-dark) 100%);
  }
  .holder-name {
    position: absolute; left: 50px; top: 178px;
    font-size: 32px; color: var(--ink-dark);
  }
  .details {
    position: absolute; left: 50px; top: 250px;
    list-style: none;
    font-size: 28px; line-height: 44px; color: var(--ink-light);
  }
  .email-rule {
    position: absolute; left: 640px; top: 500px;
    width: 360px; height: 2px; background: var(--ink-light);
  }
  .email {
    position: absolute; right: 50px; top: 512px;
    font-size: 30px; color: var(--ink-light);
  }
</style>
</head>
<body>
  <main class="card">
    <div class="ripple-decoration" role="img" aria-label="Faint concentric ripple pattern behind the card text"></div>
    <div class="ghost-name" aria-hidden="true">Amber Fox</div>

    <div class="brand">
      <span class="brand-name">Amber Fox</span>
      <span class="brand-dot"></span>
    </div>
    <div class="brand-rule"></div>

    <div class="band"></div>
    <p class="holder-name">Dennis J. Holt</p>

    <ul class="details">
      <li>Amber Fox shipping</li>
      <li>Expedited Delivery</li>
      <li>412-573-2916 fax TBD</li>
    </ul>

    <div class="email-rule"></div>
    <p class="email">dispatch@quillmail.test</p>
  </main>
</body>
</html>
```